Our companies name is The Gilded Ladle and we specialize in craft cupcakes, what I mean by that is that we bake our cupcakes with craft beer and other alcoholic drinks. We are trying to focus on being elegant but at the same time unpretentious. Since we are incorporating beer in our cupcakes we want the business card to have our logo in the front and our information in the back.

Once we select the best design we will provide the contact information to be added. Thank you.

Industry/Entity Type

Business

Font styles to use
Decorative
Script

Requirements
Must have
• Round corners
Should not have
• Square corners

```html
<!DOCTYPE html>
<html lang="en">
<head>
<meta charset="utf-8">
<title>The Gilded Ladle — Business Card</title>
<link rel="stylesheet" href="https://fonts.googleapis.com/css2?family=Arimo:wght@400;700&family=Great+Vibes&display=swap">
<style>
  :root {
    --backdrop: #c8c8c8;
    --card-white: #ffffff;
    --card-black: #0b0b0b;
    --card-black-glow: #2a2a2a;
    --ink: #2b2b2b;
    --ink-soft: #4a4a4a;
    --teal: #7fd3c6;
    --red: #e0323a;
    --shadow: rgba(0, 0, 0, 0.28);
  }
  * { box-sizing: border-box; margin: 0; padding: 0; }
  html, body {
    width: 1200px;
    height: 800px;
    overflow: hidden;
    background: var(--backdrop);
  }
  .stage {
    position: relative;
    width: 1200px;
    height: 800px;
    display: flex;
    align-items: center;
    justify-content: center;
    gap: 60px;
  }
  .card {
    position: relative;
    width: 504px;
    height: 288px;
    border-radius: 26px;
    box-shadow: 0 10px 24px var(--shadow);
    overflow: hidden;
  }
  /* Contact side */
  .card--contact {
    background: var(--card-white);
    color: var(--ink);
  }
  .contact-name {
    position: absolute;
    left: 150px;
    top: 66px;
    font-family: "Great Vibes", cursive;
    font-size: 50px;
    font-weight: 400;
    color: var(--ink);
  }
  .contact-list {
    position: absolute;
    left: 150px;
    top: 136px;
    list-style: none;
    font-family: "Arimo", Arial, sans-serif;
    font-size: 15px;
    color: var(--ink-soft);
  }
  .contact-list li {
    display: flex;
    align-items: center;
    gap: 8px;
    margin-bottom: 8px;
  }
  .contact-icon { width: 12px; height: 12px; fill: var(--ink-soft); }
  .brand-mini {
    position: absolute;
    right: 26px;
    bottom: 24px;
    display: flex;
    align-items: center;
    gap: 6px;
    font-family: "Arimo", Arial, sans-serif;
    font-weight: 700;
    font-size: 13px;
    color: var(--red);
  }
  .brand-dot {
    width: 12px; height: 12px;
    border-radius: 50%;
    background: var(--red);
  }
  /* Logo side */
  .card--brand {
    background: radial-gradient(circle at 50% 50%, var(--card-black-glow) 0%, var(--card-black) 62%);
    display: flex;
    align-items: center;
    justify-content: center;
  }
  .brand-lockup {
    display: flex;
    align-items: center;
    gap: 12px;
    font-family: "Arimo", Arial, sans-serif;
    font-weight: 700;
    font-size: 28px;
    color: var(--teal);
    letter-spacing: 0.5px;
  }
  .brand-circle {
    width: 26px; height: 26px;
    border-radius: 50%;
    background: var(--red);
  }
</style>
</head>
<body>
  <main class="stage">
    <section class="card card--contact" aria-label="Contact side">
      <h1 class="contact-name">Rosa Delgado</h1>
      <ul class="contact-list">
        <li>
          <svg class="contact-icon" viewBox="0 0 12 12" aria-hidden="true"><path d="M0 2h12v8H0z M1 3l5 4 5-4v-0.5H1z" fill-rule="evenodd"/></svg>
          hello@gildedladle.com
        </li>
        <li>
          <svg class="contact-icon" viewBox="0 0 12 12" aria-hidden="true"><path d="M2.5 0.5l2 2.5-1.2 1.3c.8 1.7 2.2 3.1 3.9 3.9L8.5 7l2.5 2-1 2.2C5.2 11 1 6.8 0.8 2z"/></svg>
          555-014-2297
        </li>
      </ul>
      <div class="brand-mini"><span class="brand-dot"></span>The Gilded Ladle</div>
    </section>

    <section class="card card--brand" aria-label="Logo side">
      <div class="brand-lockup"><span class="brand-circle"></span>The Gilded Ladle</div>
    </section>
  </main>
</body>
</html>
```